Tallow Microsystems PowerPoint Master Slide Deck Design

This is a 2-phase project to design a slide deck for a semiconductor company in the Silicon Valley. The design budget will be increased with each phase.
The slide deck will need to have one version with a dark background for presentations and a second version with a white background. Otherwise, the slides will be the same. I anticipate we will need a total of 10 slides, but that number may change.
The first phase will be to design a Title and a Title and Content slide.
- The Title Slide is the first slide of the deck. It should include the presentation title, the presenter's name and date of presentation
- The Title and Content slide should include a title and content with bullet points and up to 2 additional sub-bullets
- The Title and Content slide should have a footer that includes the slide #, Tallow Microsystems Confidential, and the logo. This footer will be on every slide except the Title Slide
The first two slides will serve as the format for the remaining ~8 slides:
-Header and Content Text (1, 2, 4 column)
-Header and Content Image (bar chart, pie chart, tables)
-Break
-Title only
-Closing (Tallow logo only)
Our slides contain a lot of content so a clean and simple design is best.
Both phases will need to include pre-set color options for
-Text and Lines
-Shadows
-Bullets and sub-bullets (including shapes, ex. circle, slash, square, etc.)
-Bar charts, pie charts, tables
Samples of our collateral are attached. Logo files are also attached
Look and feel
Each slider illustrates characteristics of the customer's brand and the style your logo design should communicate.

```html
<!DOCTYPE html>
<html lang="en">
<head>
<meta charset="utf-8">
<title>Tallow Microsystems – Master Slide Deck</title>
<link href="https://fonts.googleapis.com/css2?family=Montserrat:wght@400;500;600;700;800&display=swap" rel="stylesheet">
<style>
:root{
  --ink:#1b2130;
  --navy:#0b1a3a;
  --blue:#1a56e8;
  --cyan:#2fa8f0;
  --sky:#7cc6f7;
  --grey:#5b6270;
  --line:#d9dee6;
  --canvas:#eef0f3;
  --white:#ffffff;
}
*{margin:0;padding:0;box-sizing:border-box}
html,body{width:1200px;height:4872px;overflow:hidden;background:var(--canvas);font-family:"Montserrat",sans-serif;color:var(--ink)}
.deck{display:grid;grid-template-columns:555px 555px;column-gap:28px;row-gap:28.7px;padding:32px 0 0 32px}
.slide{position:relative;width:555px;height:312px;background:var(--white);overflow:hidden}
.abs{position:absolute}
.ph{position:absolute}
.brand{font-weight:700;letter-spacing:.5px;display:inline-flex;align-items:center;gap:5px}
.brand i{display:inline-block;width:8px;height:8px;border-radius:50%;background:currentColor}
.h{position:absolute;left:28px;top:34px;font-size:13px;font-weight:700;color:var(--ink)}
.h-r{position:absolute;left:28px;top:30px;font-size:13px;font-weight:700;color:var(--ink)}
.h-r svg{display:block;margin-top:4px}
.p{font-size:6.4px;line-height:1.5;color:#4a505c}
.ct{font-size:7.5px;font-weight:700;color:var(--cyan);margin-bottom:6px}
.bl{list-style:none}
.bl li{position:relative;padding-left:11px;margin-bottom:8px;font-size:6.4px;line-height:1.5;color:#4a505c}
.bl li::before{content:"";position:absolute;left:0;top:2px;width:6px;height:6px;border-radius:50%;background:var(--cyan);box-shadow:0 0 0 1.5px #cfe9fb}
/* footers */
.foot-d{position:absolute;left:0;right:0;bottom:0;height:24px;background:linear-gradient(var(--blue),var(--blue)) top right/80% 3px no-repeat,var(--ink);color:var(--white);font-size:6px;display:flex;align-items:center;padding:3px 16px 0 28px}
.foot-d .brand{font-size:8px}
.foot-d .conf{margin-left:auto;margin-right:150px}
.foot-b{position:absolute;left:0;right:0;bottom:0;height:24px}
.foot-b .bar{position:absolute;left:0;bottom:0;height:13px;width:100%;background:linear-gradient(90deg,var(--blue),var(--cyan) 72%,var(--blue) 100%)}
.foot-b .conf{position:absolute;left:28px;bottom:3px;font-size:6px;color:var(--white)}
.foot-b .logo{position:absolute;right:34px;bottom:4px;background:var(--white);padding:4px 8px;color:var(--blue);font-size:8px}
.foot-b .pg{position:absolute;right:10px;bottom:3px;font-size:6px;color:var(--white)}
.dark{background:var(--ink);color:var(--white)}
.cols{position:absolute;left:28px;right:28px;top:72px;display:grid;gap:18px}
</style>
</head>
<body>
<main class="deck">

<!-- 1 Title dark -->
<section class="slide dark">
  <div class="ph" style="inset:0;background:radial-gradient(circle at 70% 40%,#2b7a8c 0%,#12394a 35%,#0b1722 75%)" role="img" aria-label="Photo of a glowing processor chip on a circuit board"></div>
  <div class="ph" style="inset:0;background:linear-gradient(90deg,rgba(11,18,30,.92) 30%,rgba(11,18,30,0) 75%)"></div>
  <div class="abs brand" style="left:30px;top:40px;font-size:11px;color:var(--white)"><i></i>Tallow</div>
  <h1 class="abs" style="left:30px;top:115px;font-size:20px;line-height:1.25;font-weight:700">Presentation<br>Title Goes Here</h1>
  <div class="abs" style="left:30px;top:172px;font-size:8.5px">Presentation Subtitle Goes Here</div>
  <div class="abs" style="left:30px;top:212px;font-size:8.5px">Dec 16, 2023</div>
</section>

<!-- 2 Title dark, picture right -->
<section class="slide" style="background:#0c1220;color:var(--white)">
  <div class="ph" style="left:290px;top:0;width:265px;height:312px;background:radial-gradient(circle at 55% 45%,#3a8a4a 0%,#1c4a38 25%,#0f3a7a 55%,#0c1220 85%)" role="img" aria-label="Photo of a single-board computer with a blue light trail"></div>
  <div class="abs brand" style="left:30px;top:40px;font-size:11px;color:var(--white)"><i></i>Tallow</div>
  <h1 class="abs" style="left:30px;top:115px;font-size:20px;line-height:1.25;font-weight:700;color:var(--cyan)">Presentation<br>Title Goes Here</h1>
  <div class="abs" style="left:30px;top:172px;font-size:8.5px">Presentation Subtitle Goes Here</div>
  <div class="abs" style="left:30px;top:222px;font-size:8.5px;padding:5px 14px;border:1px solid rgba(255,255,255,.35);border-radius:3px">Dec 16, 2023</div>
</section>

<!-- 3 Title centered -->
<section class="slide dark">
  <div class="ph" style="inset:0;background:linear-gradient(180deg,#2d3440 0%,#151a24 55%,#0d111a 100%)" role="img" aria-label="Photo of a network mesh over a microchip"></div>
  <div class="abs brand" style="left:0;right:0;top:82px;justify-content:center;font-size:16px;color:var(--white)"><i></i>Tallow</div>
  <h1 class="abs" style="left:0;right:0;top:145px;text-align:center;font-size:17px;font-weight:700;letter-spacing:1px">PRESENTATION TITLE GOES HERE</h1>
  <div class="abs" style="left:0;right:0;top:178px;text-align:center;font-size:8.5px">Presentation Subtitle Goes Here</div>
  <div class="abs" style="left:214px;top:222px;width:127px;height:24px;border-radius:12px;background:var(--blue);font-size:8.5px;display:flex;align-items:center;justify-content:center">Dec 16, 2023</div>
</section>

<!-- 4 Title centered blue -->
<section class="slide dark">
  <div class="ph" style="inset:0;background:radial-gradient(ellipse at 50% 10%,#1b5fc4 0%,#0a2a66 45%,#04122e 100%)" role="img" aria-label="Photo of a blue circuit board"></div>
  <div class="abs brand" style="left:0;right:0;top:72px;justify-content:center;font-size:16px;color:var(--white)"><i></i>Tallow</div>
  <h1 class="abs" style="left:0;right:0;top:132px;text-align:center;font-size:19px;font-weight:700">Presentation Title Goes Here</h1>
  <div class="abs" style="left:0;right:0;top:162px;text-align:center;font-size:9px;color:#a8b4c8">Presentation Subtitle Goes Here</div>
  <svg class="abs" style="left:215px;top:210px" width="125" height="30" viewBox="0 0 125 30"><polygon points="12,1 113,1 124,15 113,29 12,29 1,15" fill="none" stroke="#9fb0cc" stroke-width="1"/><text x="62.5" y="18" text-anchor="middle" font-family="Montserrat,sans-serif" font-size="8.5" fill="#fff">Dec 16, 2023</text></svg>
</section>

<!-- 5 Title light -->
<section class="slide">
  <div class="ph" style="inset:0;clip-path:polygon(48% 0,100% 0,100% 100%,28% 100%);background:linear-gradient(135deg,#cfe6f4 0%,#8fb8d0 50%,#5a7a90 100%)" role="img" aria-label="Photo of a technician in a cleanroom suit holding a chip"></div>
  <svg class="abs" style="left:0;top:0" width="555" height="312"><line x1="215" y1="312" x2="252" y2="210" stroke="var(--blue)" stroke-width="2.5"/><circle cx="256" cy="202" r="6" fill="#fff" stroke="var(--blue)" stroke-width="2"/></svg>
  <div class="abs brand" style="left:40px;top:40px;font-size:14px;color:var(--blue)"><i></i>Tallow</div>
  <div class="abs" style="left:30px;top:100px;width:2px;height:42px;background:var(--blue)"></div>
  <h1 class="abs" style="left:40px;top:102px;font-size:15px;font-weight:700"><span style="color:var(--blue)">PRESENTATION</span> TITLE</h1>
  <div class="abs" style="left:40px;top:125px;font-size:8px;color:var(--grey)">Presentation Subtitle Goes Here</div>
  <div class="abs" style="left:40px;top:276px;font-size:8px">Dec 16, 2023</div>
</section>

<!-- 6 Title light chevron -->
<section class="slide">
  <svg class="abs" style="left:0;top:0" width="555" height="312" viewBox="0 0 555 312">
    <polygon points="160,0 555,0 555,140 440,262 400,262 280,140" fill="var(--blue)"/>
  </svg>
  <div class="ph" style="left:0;top:0;width:555px;height:312px;clip-path:polygon(180px 0,555px 0,555px 120px,440px 240px,300px 118px);background:linear-gradient(160deg,#0b2a4a 0%,#10506e 45%,#3fc3e8 100%)" role="img" aria-label="Photo of a circuit board with rising light streaks"></div>
  <div class="abs brand" style="left:36px;top:150px;font-size:14px;color:var(--blue)"><i></i>Tallow</div>
  <h1 class="abs" style="left:36px;top:215px;font-size:15px;font-weight:700"><span style="color:var(--blue)">PRESENTATION</span> TITLE</h1>
  <div class="abs" style="left:36px;top:238px;font-size:8px;color:var(--grey)">Presentation Subtitle Goes Here</div>
  <div class="abs" style="left:36px;top:270px;font-size:8px"><span style="color:var(--blue);font-weight:700">»</span>&nbsp; Dec 16, 2023</div>
</section>

<!-- 7 Agenda -->
<section class="slide">
  <div class="h">Agenda</div>
  <div class="ph" style="left:0;top:76px;width:300px;height:176px;clip-path:polygon(0 0,100% 0,88% 100%,0 100%);background:radial-gradient(circle at 45% 50%,#7fd0ff 0%,#1a5fc0 30%,#0a1a3c 75%)" role="img" aria-label="Photo of a glowing processor on a blue board"></div>
  <svg class="abs" style="left:0;top:0" width="555" height="312" font-family="Montserrat,sans-serif" font-size="6.5">
    <g fill="var(--blue)"><polygon points="318,96 348,96 344,110 314,110"/><polygon points="303,128 333,128 329,142 299,142"/><polygon points="290,160 320,160 316,174 286,174"/><polygon points="278,192 308,192 304,206 274,206"/><polygon points="268,224 298,224 294,238 264,238"/></g>
    <g fill="#fff" font-weight="700" text-anchor="middle"><text x="331" y="105.5">1</text><text x="316" y="137.5">2</text><text x="303" y="169.5">3</text><text x="291" y="201.5">4</text><text x="281" y="233.5">5</text></g>
    <g stroke="var(--line)"><line x1="348" y1="110" x2="520" y2="110"/><line x1="333" y1="142" x2="520" y2="142"/><line x1="320" y1="174" x2="520" y2="174"/><line x1="308" y1="206" x2="520" y2="206"/><line x1="298" y1="238" x2="520" y2="238"/></g>
    <g fill="#333"><text x="375" y="106">Market outlook and key goals</text><text x="360" y="138">Wafer yield and fab updates</text><text x="347" y="170">Product roadmap review</text><text x="335" y="202">Customer and partner news</text><text x="325" y="234">Next steps and open items</text></g>
  </svg>
  <div class="foot-d"><span class="brand"><i></i>Tallow</span><span class="conf">Tallow Microsystems Confidential</span><span>2</span></div>
</section>

<!-- 8 Text slide -->
<section class="slide">
  <div class="h-r">Text Slide<svg width="22" height="6"><line x1="0" y1="3" x2="18" y2="3" stroke="var(--blue)" stroke-width="1.5"/><circle cx="3" cy="3" r="2.5" fill="var(--blue)"/><polyline points="16,0.5 20,3 16,5.5" fill="none" stroke="var(--blue)" stroke-width="1.2"/></svg></div>
  <div class="abs" style="left:50px;right:50px;top:78px">
    <p class="p" style="margin-bottom:10px"><span style="color:var(--blue);font-weight:600">Our process team refined the wafer flow this quarter.</span> Yield rose on every fab line while cycle time fell and defect rates held low. Quality stayed steady for key customers in each region, and the new test cell is now fully qualified for volume output with stable results across all lots shipped this term.</p>
    <ul class="bl" style="margin-bottom:8px">
      <li>Yield improved across all lines, with the largest gain on the mature node and fewer scrapped lots.</li>
      <li>New packaging partner cut lead time by two weeks and lowered cost per unit for the main product family.</li>
      <li>Design wins grew in automotive and industrial markets, adding strong demand for the next two quarters.</li>
    </ul>
    <p class="p">Looking ahead, the team will expand capacity on the current node, finish the next test cell, and prepare samples for early customers. Updates will follow in the next review with full data for each product line and region.</p>
  </div>
  <div class="foot-b"><div class="bar"></div><span class="conf">Tallow Microsystems Confidential</span><span class="logo brand"><i></i>Tallow</span><span class="pg">2</span></div>
</section>

<!-- 9 One column -->
<section class="slide">
  <div class="h">One Column Text</div>
  <div class="abs" style="left:28px;top:82px;width:285px">
    <p class="p" style="margin-bottom:9px">Our process team refined the wafer flow this quarter. Yield rose on every fab line while cycle time fell and defect rates held low, and quality stayed steady for key customers in each region.</p>
    <p class="p" style="margin-bottom:9px">The new test cell is now qualified for volume output with stable results across all lots shipped this term, and the packaging partner cut lead time by two weeks.</p>
    <p class="p">Design wins grew in automotive and industrial markets, adding strong demand for the next two quarters and a healthy outlook.</p>
  </div>
  <div class="ph" style="left:335px;top:80px;width:160px;height:130px;background:radial-gradient(circle,#dfe7f5 0%,#fff 70%)" role="img" aria-label="Decorative circuit node graphic"></div>
  <div class="foot-d"><span class="brand"><i></i>Tallow</span><span class="conf">Tallow Microsystems Confidential</span><span>2</span></div>
</section>

<!-- 10 Two column -->
<section class="slide">
  <div class="h-r">Two Column Text<svg width="22" height="6"><line x1="0" y1="3" x2="18" y2="3" stroke="var(--blue)" stroke-width="1.5"/><circle cx="3" cy="3" r="2.5" fill="var(--blue)"/><polyline points="16,0.5 20,3 16,5.5" fill="none" stroke="var(--blue)" stroke-width="1.2"/></svg></div>
  <div class="cols" style="grid-template-columns:1fr 1fr;gap:28px;top:90px">
    <p class="p">Our process team refined the wafer flow this quarter. Yield rose on every fab line while cycle time fell and defect rates held low. Quality stayed steady for key customers in each region, and the new test cell is qualified for volume output with stable results. The packaging partner cut lead time by two weeks and lowered unit cost for the main product family, while design wins grew in automotive and industrial markets.</p>
    <p class="p">Looking ahead, the team will expand capacity on the current node, finish the next test cell, and prepare samples for early customers. Updates will follow in the next review with full data for each product line and region. Demand remains strong for the next two quarters and the supply plan covers all committed orders with room for growth in each key market segment.</p>
  </div>
  <div class="foot-b"><div class="bar"></div><span class="conf">Tallow Microsystems Confidential</span><span class="logo brand"><i></i>Tallow</span><span class="pg">2</span></div>
</section>

<!-- 11 Three column -->
<section class="slide">
  <div class="h">Three Column Text</div>
  <div class="cols" style="grid-template-columns:1fr 1fr 1fr;top:90px">
    <div><div class="ct">Content Title</div><p class="p">Our process team refined the wafer flow this quarter. Yield rose on every fab line while cycle time fell and defect rates held low. Quality stayed steady for key customers in each region and the new test cell is ready for volume output.</p></div>
    <div><div class="ct">Content Title</div><p class="p">Our process team refined the wafer flow this quarter. Yield rose on every fab line while cycle time fell and defect rates held low. Quality stayed steady for key customers in each region and the new test cell is ready for volume output.</p></div>
    <div><div class="ct">Content Title</div><p class="p">Our process team refined the wafer flow this quarter. Yield rose on every fab line while cycle time fell and defect rates held low. Quality stayed steady for key customers in each region and the new test cell is ready for volume output.</p></div>
  </div>
  <div class="foot-d"><span class="brand"><i></i>Tallow</span><span class="conf">Tallow Microsystems Confidential</span><span>2</span></div>
</section>

<!-- 12 Four column -->
<section class="slide">
  <div class="h-r">Four Column Text<svg width="22" height="6"><line x1="0" y1="3" x2="18" y2="3" stroke="var(--blue)" stroke-width="1.5"/><circle cx="3" cy="3" r="2.5" fill="var(--blue)"/><polyline points="16,0.5 20,3 16,5.5" fill="none" stroke="var(--blue)" stroke-width="1.2"/></svg></div>
  <div class="cols" style="grid-template-columns:repeat(4,1fr);top:80px;gap:16px;text-align:center">
    <div><svg width="18" height="18"><circle cx="9" cy="9" r="9" fill="var(--blue)"/><circle cx="9" cy="9" r="4" fill="none" stroke="#fff" stroke-width="1.5"/></svg><div class="ct" style="margin-top:4px">Content Title</div><p class="p" style="text-align:justify">Yield rose on every fab line while cycle time fell and defect rates held low. Quality stayed steady for key customers in each region, and the new test cell is ready for volume output with stable results.</p></div>
    <div><svg width="18" height="18"><circle cx="9" cy="9" r="9" fill="var(--blue)"/><rect x="5" y="5" width="8" height="8" fill="none" stroke="#fff" stroke-width="1.5"/></svg><div class="ct" style="margin-top:4px">Content Title</div><p class="p" style="text-align:justify">Yield rose on every fab line while cycle time fell and defect rates held low. Quality stayed steady for key customers in each region, and the new test cell is ready for volume output with stable results.</p></div>
    <div><svg width="18" height="18"><circle cx="9" cy="9" r="9" fill="var(--blue)"/><circle cx="9" cy="7" r="2.5" fill="#fff"/><rect x="5" y="10.5" width="8" height="3.5" rx="1.5" fill="#fff"/></svg><div class="ct" style="margin-top:4px">Content Title</div><p class="p" style="text-align:justify">Yield rose on every fab line while cycle time fell and defect rates held low. Quality stayed steady for key customers in each region, and the new test cell is ready for volume output with stable results.</p></div>
    <div><svg width="18" height="18"><circle cx="9" cy="9" r="9" fill="var(--blue)"/><path d="M9 4 a3.5 3.5 0 0 1 2 6.4 V12 H7 V10.4 A3.5 3.5 0 0 1 9 4z" fill="#fff"/></svg><div class="ct" style="margin-top:4px">Content Title</div><p class="p" style="text-align:justify">Yield rose on every fab line while cycle time fell and defect rates held low. Quality stayed steady for key customers in each region, and the new test cell is ready for volume output with stable results.</p></div>
  </div>
  <div class="foot-b"><div class="bar"></div><span class="conf">Tallow Microsystems Confidential</span><span class="logo brand"><i></i>Tallow</span><span class="pg">2</span></div>
</section>

<!-- 13 Text and picture -->
<section class="slide">
  <div class="h">Text and Picture</div>
  <ul class="bl abs" style="left:56px;top:88px;width:210px">
    <li>Yield rose on every fab line while cycle time fell and defect rates held low this term.</li>
    <li>The new test cell is now qualified for volume output with stable results across lots.</li>
    <li>Packaging partner cut lead time by two weeks and lowered unit cost for main products.</li>
    <li>Design wins grew in automotive and industrial markets for the next two quarters.</li>
  </ul>
  <div class="ph" style="left:300px;top:84px;width:228px;height:148px;background:linear-gradient(135deg,#e9eef3 0%,#b8c4cf 50%,#6f7d8a 100%)" role="img" aria-label="Photo of a wafer inspection microscope in a lab"></div>
  <div class="foot-d"><span class="brand"><i></i>Tallow</span><span class="conf">Tallow Microsystems Confidential</span><span>2</span></div>
</section>

<!-- 14 Picture and text -->
<section class="slide">
  <div class="ph" style="left:0;top:0;width:232px;height:288px;background:linear-gradient(180deg,#3a4550 0%,#8a98a6 45%,#2a3440 100%)" role="img" aria-label="Photo of a precision machining tool"></div>
  <div class="h-r" style="left:282px">Text and Picture<svg width="22" height="6"><line x1="0" y1="3" x2="18" y2="3" stroke="var(--blue)" stroke-width="1.5"/><circle cx="3" cy="3" r="2.5" fill="var(--blue)"/><polyline points="16,0.5 20,3 16,5.5" fill="none" stroke="var(--blue)" stroke-width="1.2"/></svg></div>
  <div class="abs" style="left:282px;top:84px;width:240px">
    <div class="ct" style="margin-bottom:2px;font-size:6.5px">Descriptions</div>
    <p class="p" style="margin-bottom:10px">Yield rose on every fab line while cycle time fell and defect rates held low for key lots.</p>
    <div class="ct" style="margin-bottom:4px;font-size:6.5px">Details</div>
    <ul class="bl" style="margin-bottom:8px"><li>New test cell qualified for volume output.</li><li>Lead time cut by two weeks with new partner.</li><li>Design wins grew in automotive and industrial markets this term.</li></ul>
    <div style="font-size:6.5px;font-weight:600;margin-bottom:2px">Others</div>
    <p class="p">Quality stayed steady for key customers in each region through the quarter.</p>
  </div>
  <div class="foot-b"><div class="bar"></div><span class="conf">Tallow Microsystems Confidential</span><span class="logo brand"><i></i>Tallow</span><span class="pg">2</span></div>
</section>

<!-- 15 Break -->
<section class="slide dark">
  <div class="ph" style="inset:0;background:radial-gradient(circle at 60% 40%,#2c4a50 0%,#16262c 55%,#0b1216 100%)" role="img" aria-label="Photo of a dark circuit board"></div>
  <div class="abs brand" style="left:30px;top:150px;font-size:12px;color:var(--white)"><i></i>Tallow</div>
  <h1 class="abs" style="left:30px;top:170px;font-size:32px;font-weight:800">Break Slide</h1>
  <div class="abs" style="left:30px;top:214px;font-size:10px;color:#b5c0c8">Your Subtitle Goes Here</div>
</section>

<!-- 16 Slide break -->
<section class="slide dark">
  <div class="ph" style="inset:0;background:radial-gradient(circle at 40% 60%,#34393f 0%,#1c2025 60%,#111418 100%)" role="img" aria-label="Photo of a dark printed circuit board"></div>
  <div class="abs brand" style="left:30px;top:36px;font-size:12px;color:var(--white)"><i></i>Tallow</div>
  <div class="abs" style="left:296px;top:192px;font-size:54px;font-weight:800;color:rgba(255,255,255,.12)">01</div>
  <h1 class="abs" style="left:352px;top:196px;font-size:32px;line-height:1.15;font-weight:800;letter-spacing:1px">SLIDE<br>BREAK</h1>
</section>

<!-- 17 Text and picture strip -->
<section class="slide">
  <div class="h">Text and Picture</div>
  <p class="p abs" style="left:28px;top:66px;width:330px">Yield rose on every fab line while cycle time fell and defect rates held low for key customers this quarter.</p>
  <div class="abs" style="left:0;top:124px;width:555px;height:136px;display:grid;grid-template-columns:repeat(4,1fr)">
    <div class="ph" style="position:static;background:linear-gradient(135deg,#2c3e50,#5d7083)" role="img" aria-label="Photo of a board under test"></div>
    <div class="ph" style="position:static;background:linear-gradient(135deg,#d7e4ef,#8aa6bf)" role="img" aria-label="Photo of a cleanroom"></div>
    <div class="ph" style="position:static;background:linear-gradient(135deg,#b9c9d8,#4e6277)" role="img" aria-label="Photo of lab equipment"></div>
    <div class="ph" style="position:static;background:linear-gradient(135deg,#3a4450,#1a2230)" role="img" aria-label="Photo of an engineer at work"></div>
  </div>
  <div class="foot-d"><span class="brand"><i></i>Tallow</span><span class="conf">Tallow Microsystems Confidential</span><span>2</span></div>
</section>

<!-- 18 Laptop mockup -->
<section class="slide">
  <div class="h-r">Laptop Mockup<svg width="22" height="6"><line x1="0" y1="3" x2="18" y2="3" stroke="var(--blue)" stroke-width="1.5"/><circle cx="3" cy="3" r="2.5" fill="var(--blue)"/><polyline points="16,0.5 20,3 16,5.5" fill="none" stroke="var(--blue)" stroke-width="1.2"/></svg></div>
  <div class="ph" style="left:28px;top:92px;width:262px;height:160px;background:linear-gradient(180deg,#1d3f8a 0%,#0a1a3a 78%,#c9ced6 80%,#e8ebef 100%)" role="img" aria-label="Laptop showing a chip on its screen"></div>
  <svg class="abs" style="left:300px;top:92px" width="240" height="170" font-family="Montserrat,sans-serif">
    <circle cx="33" cy="14" r="11" fill="var(--blue)"/><text x="33" y="17" font-size="8" fill="#fff" text-anchor="middle" font-weight="700">1</text>
    <circle cx="33" cy="77" r="11" fill="var(--cyan)"/><text x="33" y="80" font-size="8" fill="#fff" text-anchor="middle" font-weight="700">2</text>
    <circle cx="33" cy="140" r="11" fill="var(--ink)"/><text x="33" y="143" font-size="8" fill="#fff" text-anchor="middle" font-weight="700">3</text>
    <g font-size="7.5" font-weight="700"><text x="62" y="6" fill="var(--blue)">Content Title</text><text x="62" y="69" fill="var(--cyan)">Content Title</text><text x="62" y="132" fill="var(--ink)">Content Title</text></g>
    <g font-size="6" fill="#4a505c"><text x="62" y="18">Yield rose on every fab line this</text><text x="62" y="26">term, with fewer scrapped lots.</text><text x="62" y="81">Lead time fell by two weeks with</text><text x="62" y="89">our new packaging partner.</text><text x="62" y="144">Design wins grew in automotive</text><text x="62" y="152">and industrial markets.</text></g>
  </svg>
  <div class="foot-b"><div class="bar"></div><span class="conf">Tallow Microsystems Confidential</span><span class="logo brand"><i></i>Tallow</span><span class="pg">2</span></div>
</section>

<!-- 19 Blank -->
<section class="slide">
  <div class="h">Blank Slide</div>
  <div class="ph" style="left:290px;top:70px;width:240px;height:180px;background:radial-gradient(circle,#e4ecfa 0%,#fff 70%)" role="img" aria-label="Faint decorative circuit node graphic"></div>
  <div class="foot-d"><span class="brand"><i></i>Tallow</span><span class="conf">Tallow Microsystems Confidential</span><span>2</span></div>
</section>

<!-- 20 Picture with section -->
<section class="slide">
  <div class="ph" style="left:0;top:0;width:555px;height:150px;background:linear-gradient(120deg,#141a22 0%,#2c3642 55%,#101419 100%)" role="img" aria-label="Photo of a chip on a dark circuit board"></div>
  <div class="abs" style="left:28px;top:36px;font-size:13px;font-weight:700;color:var(--white)">Picture with Section</div>
  <svg class="abs" style="left:28px;top:54px" width="22" height="6"><line x1="0" y1="3" x2="18" y2="3" stroke="#fff" stroke-width="1.5"/><circle cx="3" cy="3" r="2.5" fill="#fff"/></svg>
  <div class="abs" style="left:28px;right:28px;top:118px;display:grid;grid-template-columns:repeat(3,1fr);text-align:center">
    <div><div style="margin:0 auto;width:86px;height:86px;border-radius:50%;border:3px solid #fff;background:radial-gradient(circle,#5a9ad8,#14325c)" role="img" aria-label="Photo of a processor"></div><div class="ct" style="margin:6px 0 3px">Content Title</div><p class="p">Yield rose on every line<br>with fewer scrapped lots</p></div>
    <div><div style="margin:0 auto;width:86px;height:86px;border-radius:50%;border:3px solid #fff;background:radial-gradient(circle,#8a939c,#2a3138)" role="img" aria-label="Photo of a chip socket"></div><div class="ct" style="margin:6px 0 3px">Content Title</div><p class="p">Yield rose on every line<br>with fewer scrapped lots</p></div>
    <div><div style="margin:0 auto;width:86px;height:86px;border-radius:50%;border:3px solid #fff;background:radial-gradient(circle,#6b8a7a,#1f2c28)" role="img" aria-label="Photo of a circuit board"></div><div class="ct" style="margin:6px 0 3px">Content Title</div><p class="p">Yield rose on every line<br>with fewer scrapped lots</p></div>
  </div>
  <div class="foot-b"><div class="bar"></div><span class="conf">Tallow Microsystems Confidential</span><span class="logo brand"><i></i>Tallow</span><span class="pg">2</span></div>
</section>

<!-- 21 Timeline -->
<section class="slide">
  <div class="h">Timeline</div>
  <svg class="abs" style="left:0;top:0" width="555" height="312" font-family="Montserrat,sans-serif">
    <g fill="var(--ink)">
      <polygon points="60,164 142,164 132,180 50,180"/><polygon points="155,164 237,164 227,180 145,180"/><polygon points="250,164 332,164 322,180 240,180"/><polygon points="345,164 427,164 417,180 335,180"/><polygon points="440,164 522,164 512,180 430,180"/>
    </g>
    <g fill="var(--blue)"><polygon points="142,164 155,164 145,180 132,180"/><polygon points="237,164 250,164 240,180 227,180"/><polygon points="332,164 345,164 335,180 322,180"/><polygon points="427,164 440,164 430,180 417,180"/></g>
    <g fill="#fff" font-size="8" font-weight="700" text-anchor="middle"><text x="96" y="175">2019</text><text x="191" y="175">2020</text><text x="286" y="175">2021</text><text x="381" y="175">2022</text><text x="476" y="175">2023</text></g>
    <g font-size="6" fill="#4a505c" text-anchor="middle">
      <text x="96" y="198">Pilot fab line</text><text x="96" y="206">opened in the</text><text x="96" y="214">valley campus</text>
      <text x="191" y="128">First product</text><text x="191" y="136">shipped to lead</text><text x="191" y="144">auto customer</text>
      <text x="286" y="198">Test cell and</text><text x="286" y="206">yield program</text><text x="286" y="214">fully launched</text>
      <text x="381" y="128">Second node</text><text x="381" y="136">ramped to full</text><text x="381" y="144">volume output</text>
      <text x="476" y="198">New packaging</text><text x="476" y="206">partner signed</text><text x="476" y="214">for all lines</text>
    </g>
  </svg>
  <div class="foot-d"><span class="brand"><i></i>Tallow</span><span class="conf">Tallow Microsystems Confidential</span><span>2</span></div>
</section>

<!-- 22 Bar chart -->
<section class="slide">
  <div class="h-r">Bar Chart<svg width="22" height="6"><line x1="0" y1="3" x2="18" y2="3" stroke="var(--blue)" stroke-width="1.5"/><circle cx="3" cy="3" r="2.5" fill="var(--blue)"/><polyline points="16,0.5 20,3 16,5.5" fill="none" stroke="var(--blue)" stroke-width="1.2"/></svg></div>
  <div class="abs" style="left:50px;top:112px;width:160px">
    <p class="p" style="margin-bottom:8px">Yield rose on every fab line while cycle time fell and defect rates held low.</p>
    <p class="p" style="margin-bottom:8px">Quality stayed steady for key customers in each region this quarter.</p>
    <p class="p" style="color:var(--cyan)">Output grew each month across the first half of the year.</p>
  </div>
  <svg class="abs" style="left:250px;top:60px" width="290" height="210" font-family="Montserrat,sans-serif" font-size="6.5">
    <defs><linearGradient id="barfill" x1="0" y1="1" x2="0" y2="0"><stop offset="0" stop-color="var(--blue)"/><stop offset="1" stop-color="var(--cyan)"/></linearGradient></defs>
    <g fill="#edf0f5"><rect x="15" y="10" width="26" height="155"/><rect x="61" y="10" width="26" height="155"/><rect x="107" y="10" width="26" height="155"/><rect x="153" y="10" width="26" height="155"/><rect x="199" y="10" width="26" height="155"/><rect x="245" y="10" width="26" height="155"/></g>
    <g fill="url(#barfill)"><rect x="15" y="140" width="26" height="25"/><rect x="61" y="125" width="26" height="40"/><rect x="107" y="118" width="26" height="47"/><rect x="153" y="100" width="26" height="65"/><rect x="199" y="80" width="26" height="85"/><rect x="245" y="62" width="26" height="103"/></g>
    <g fill="#fff" font-weight="700" text-anchor="middle"><text x="28" y="153">10%</text><text x="74" y="153">20%</text><text x="120" y="153">30%</text><text x="166" y="153">40%</text><text x="212" y="153">50%</text><text x="258" y="153">60%</text></g>
    <g fill="#4a505c" text-anchor="middle"><text x="28" y="178">Jan</text><text x="74" y="178">Feb</text><text x="120" y="178">Mar</text><text x="166" y="178">Apr</text><text x="212" y="178">May</text><text x="258" y="178">Jun</text></g>
  </svg>
  <div class="foot-b"><div class="bar"></div><span class="conf">Tallow Microsystems Confidential</span><span class="logo brand"><i></i>Tallow</span><span class="pg">2</span></div>
</section>

<!-- 23 Bar chart with stats -->
<section class="slide">
  <div class="h">Bar Chart</div>
  <p class="p abs" style="left:56px;top:110px;width:210px">Yield rose on every fab line while cycle time fell and defect rates held low. Quality stayed steady for key customers in each region this quarter and the test cell is ready.</p>
  <div class="abs" style="left:56px;top:160px;width:210px;height:64px;display:grid;grid-template-columns:repeat(3,1fr);color:#fff">
    <div style="background:var(--ink);padding:6px"><div style="font-size:12px;font-weight:700;color:var(--cyan)">3.5M</div><div style="font-size:5px;line-height:1.4;margin-top:3px">Units shipped in the first half of the year</div></div>
    <div style="background:var(--blue);padding:6px"><div style="font-size:12px;font-weight:700">5.6M</div><div style="font-size:5px;line-height:1.4;margin-top:3px">Units shipped in the first half of the year</div></div>
    <div style="background:var(--ink);padding:6px"><div style="font-size:12px;font-weight:700">6.8M</div><div style="font-size:5px;line-height:1.4;margin-top:3px">Units shipped in the first half of the year</div></div>
  </div>
  <svg class="abs" style="left:340px;top:70px" width="200" height="180" font-family="Montserrat,sans-serif" font-size="5.5" fill="#4a505c">
    <g stroke="#e3e7ee"><line x1="24" y1="10" x2="195" y2="10"/><line x1="24" y1="26" x2="195" y2="26"/><line x1="24" y1="42" x2="195" y2="42"/><line x1="24" y1="58" x2="195" y2="58"/><line x1="24" y1="74" x2="195" y2="74"/><line x1="24" y1="90" x2="195" y2="90"/><line x1="24" y1="106" x2="195" y2="106"/><line x1="24" y1="122" x2="195" y2="122"/><line x1="24" y1="138" x2="195" y2="138"/><line x1="24" y1="154" x2="195" y2="154"/></g>
    <g><text x="0" y="12">100%</text><text x="3" y="28">90%</text><text x="3" y="44">80%</text><text x="3" y="60">70%</text><text x="3" y="76">60%</text><text x="3" y="92">50%</text><text x="3" y="108">40%</text><text x="3" y="124">30%</text><text x="3" y="140">20%</text><text x="3" y="156">10%</text></g>
    <g fill="var(--ink)"><rect x="32" y="60" width="7" height="110"/><rect x="56" y="40" width="7" height="130"/><rect x="80" y="70" width="7" height="100"/><rect x="104" y="30" width="7" height="140"/><rect x="128" y="55" width="7" height="115"/><rect x="152" y="35" width="7" height="135"/><rect x="176" y="48" width="7" height="122"/></g>
    <g fill="var(--blue)"><rect x="41" y="90" width="7" height="80"/><rect x="65" y="70" width="7" height="100"/><rect x="89" y="50" width="7" height="120"/><rect x="113" y="80" width="7" height="90"/><rect x="137" y="45" width="7" height="125"/><rect x="161" y="75" width="7" height="95"/><rect x="185" y="30" width="7" height="140"/></g>
    <line x1="24" y1="170" x2="195" y2="170" stroke="#9aa3b0"/>
  </svg>
  <div class="foot-d"><span class="brand"><i></i>Tallow</span><span class="conf">Tallow Microsystems Confidential</span><span>2</span></div>
</section>

<!-- 24 Pie charts -->
<section class="slide">
  <div class="h-r">Pie Charts<svg width="22" height="6"><line x1="0" y1="3" x2="18" y2="3" stroke="var(--blue)" stroke-width="1.5"/><circle cx="3" cy="3" r="2.5" fill="var(--blue)"/><polyline points="16,0.5 20,3 16,5.5" fill="none" stroke="var(--blue)" stroke-width="1.2"/></svg></div>
  <p class="p abs" style="left:120px;width:315px;top:68px;text-align:center">Yield rose on every fab line while cycle time fell and defect rates held low. Quality stayed steady for key customers in each region this quarter and the new test cell is ready for volume output.</p>
  <svg class="abs" style="left:0;top:0" width="555" height="312" font-family="Montserrat,sans-serif">
    <g fill="none" stroke-width="6">
      <circle cx="147" cy="175" r="28" stroke="#e6eaf0"/><circle cx="147" cy="175" r="28" stroke="var(--blue)" stroke-dasharray="52.8 175.9" transform="rotate(-90 147 175)"/>
      <circle cx="277" cy="175" r="28" stroke="#e6eaf0"/><circle cx="277" cy="175" r="28" stroke="var(--cyan)" stroke-dasharray="88 175.9" transform="rotate(-90 277 175)"/>
      <circle cx="407" cy="175" r="28" stroke="#e6eaf0"/><circle cx="407" cy="175" r="28" stroke="var(--ink)" stroke-dasharray="140.7 175.9" transform="rotate(-90 407 175)"/>
    </g>
    <g font-size="14" font-weight="700" text-anchor="middle"><text x="147" y="180" fill="var(--blue)">30%</text><text x="277" y="180" fill="var(--cyan)">50%</text><text x="407" y="180" fill="var(--ink)">80%</text></g>
    <g font-size="6" fill="#4a505c" text-anchor="middle"><text x="147" y="226">Yield gain on the</text><text x="147" y="234">mature node line</text><text x="277" y="226">Share of orders</text><text x="277" y="234">from auto market</text><text x="407" y="226">Capacity used in</text><text x="407" y="234">the first half year</text></g>
  </svg>
  <div class="foot-b"><div class="bar"></div><span class="conf">Tallow Microsystems Confidential</span><span class="logo brand"><i></i>Tallow</span><span class="pg">2</span></div>
</section>

<!-- 25 Infographic -->
<section class="slide">
  <div class="h">Infographic</div>
  <svg class="abs" style="left:0;top:0" width="555" height="312" font-family="Montserrat,sans-serif">
    <polygon points="283,110 245,178 323,178" fill="var(--ink)"/>
    <circle cx="283" cy="110" r="30" fill="var(--blue)"/>
    <circle cx="245" cy="178" r="30" fill="var(--sky)"/>
    <circle cx="323" cy="178" r="30" fill="var(--ink)"/>
    <circle cx="283" cy="110" r="17" fill="#fff"/><circle cx="245" cy="178" r="17" fill="#fff"/><circle cx="323" cy="178" r="17" fill="#fff"/>
    <g fill="none" stroke="var(--blue)" stroke-width="1.5"><rect x="277" y="104" width="12" height="12"/><circle cx="245" cy="178" r="5"/><polyline points="317,178 321,182 329,173" stroke="var(--ink)"/></g>
    <g font-size="7.5" font-weight="700"><text x="283" y="68" text-anchor="middle" fill="var(--blue)">Content Title</text><text x="212" y="232" fill="var(--sky)">Content Title</text><text x="350" y="232" fill="var(--ink)">Content Title</text></g>
  </svg>
  <div class="foot-d"><span class="brand"><i></i>Tallow</span><span class="conf">Tallow Microsystems Confidential</span><span>2</span></div>
</section>

<!-- 26 Table -->
<section class="slide">
  <div class="h-r">Table<svg width="22" height="6"><line x1="0" y1="3" x2="18" y2="3" stroke="var(--blue)" stroke-width="1.5"/><circle cx="3" cy="3" r="2.5" fill="var(--blue)"/><polyline points="16,0.5 20,3 16,5.5" fill="none" stroke="var(--blue)" stroke-width="1.2"/></svg></div>
  <svg class="abs" style="left:88px;top:92px" width="450" height="160" font-family="Montserrat,sans-serif" font-size="6">
    <rect x="0" y="0" width="112" height="20" fill="#e8ebef"/><rect x="112" y="0" width="112" height="20" fill="var(--blue)"/><rect x="224" y="0" width="112" height="20" fill="var(--cyan)"/><rect x="336" y="0" width="112" height="20" fill="var(--ink)"/>
    <g font-weight="700" text-anchor="middle"><text x="56" y="13" fill="var(--ink)">Table</text><text x="168" y="13" fill="#fff">Column 1</text><text x="280" y="13" fill="#fff">Column 2</text><text x="392" y="13" fill="#fff">Column 3</text></g>
    <g stroke="#dfe3ea"><line x1="0" y1="44" x2="448" y2="44"/><line x1="0" y1="68" x2="448" y2="68"/><line x1="0" y1="92" x2="448" y2="92"/><line x1="0" y1="116" x2="448" y2="116"/><line x1="0" y1="140" x2="448" y2="140" stroke="var(--ink)"/></g>
    <g fill="#4a505c" text-anchor="middle">
      <text x="56" y="35">Item one</text><text x="168" y="35">Item one</text><text x="280" y="35">Item one</text><text x="392" y="35">Item one</text>
      <text x="56" y="59">Item two</text><text x="168" y="59">Item two</text><text x="280" y="59">Item two</text><text x="392" y="59">Item two</text>
      <text x="56" y="83">Item three</text><text x="168" y="83">Item three</text><text x="280" y="83">Item three</text><text x="392" y="83">Item three</text>
      <text x="56" y="107">Item four</text><text x="168" y="107">Item four</text><text x="280" y="107">Item four</text><text x="392" y="107">Item four</text>
      <text x="56" y="131">Item five</text><text x="168" y="131">Item five</text><text x="280" y="131">Item five</text><text x="392" y="131">Item five</text>
    </g>
    <g font-weight="700" fill="var(--ink)" text-anchor="middle"><text x="56" y="155">Total</text><text x="168" y="155">Total</text><text x="280" y="155">Total</text><text x="392" y="155">Total</text></g>
  </svg>
  <div class="foot-b"><div class="bar"></div><span class="conf">Tallow Microsystems Confidential</span><span class="logo brand"><i></i>Tallow</span><span class="pg">2</span></div>
</section>

<!-- 27 Icons -->
<section class="slide">
  <div class="h">Icons</div>
  <svg class="abs" style="left:28px;top:62px" width="500" height="220">
    <defs>
      <pattern id="icon-set" width="50" height="20" patternUnits="userSpaceOnUse">
        <g fill="none" stroke="var(--blue)" stroke-width="1">
          <rect x="3" y="4" width="9" height="9" rx="1"/>
          <circle cx="21.5" cy="8.5" r="4.5"/>
          <path d="M31 13 L35.5 4 L40 13 Z"/>
          <path d="M45 5 V12 M41.5 8.5 H48.5"/>
        </g>
      </pattern>
    </defs>
    <rect width="500" height="220" fill="url(#icon-set)"/>
  </svg>
  <div class="foot-d"><span class="brand"><i></i>Tallow</span><span class="conf">Tallow Microsystems Confidential</span><span>2</span></div>
</section>

<!-- 28 Closing -->
<section class="slide">
  <div class="ph" style="left:330px;top:0;width:225px;height:312px;background:radial-gradient(circle at 60% 40%,#e6eefb 0%,#fff 70%)" role="img" aria-label="Faint decorative circuit node graphic"></div>
  <div class="abs brand" style="left:0;right:0;top:142px;justify-content:center;font-size:26px;color:var(--blue)"><i style="width:14px;height:14px"></i>Tallow</div>
</section>

</main>
</body>
</html>
```